Nutritional neuroscience book cover design*

We need a book cover design for a new book on nutritional neuroscience and aging. The book is written for the general public and answers questions such as, "We are living longer than ever. The problem is, will our brain stay healthy as we age? We certainly do not want to live longer with various diseases, in particular brain diseases. How does the brain change during aging? And what can we do to promote the health of our brain and prevent and treat neurological diseases that typically occur during the aging process?" Based on recent discoveries in the field of nutritional neuroscience, this book presents how we can use nutrition to help our brain stay healthy longer. While our brain shrinks and becomes functionally weaker during the aging process, nutrition is able to slow this process down. This book illustrates this point through chapters on stroke, Parkinson’s disease, Multiple Sclerosis, dementia, depression, anxiety, and schizophrenia. The book will appeal to anyone looking to optimize their brain’s health and performance today and decades into the future.

Target Market(s)

General audience

Colors

Designer to choose colors to be used in the design.

Requirements
Must have
• Title: Meals Across the Decades: A Companion Guide to Dietary Brain Science Today
• Edited by Odelia R. Vantrosk, Ph.D.
• Book size: 7*10 inches
• Backcover text:
• Humans are living longer than ever. How does the brain change during aging? Will our brain stay healthy as we age? We certainly do not want to live longer with neurological diseases. What can we do to promote the health of our brain?
• Based on recent discoveries in the field of nutritional neuroscience, this book presents how nutrition affects our brain health. While we age, our brain shrinks and there are changes in how it functions, nutrition is an important component that can help maintain optimal brain health.
• Using scientific evidence, this book illustrates the importance of nutrition for neurological diseases including Alzheimer’s disease, stroke, Parkinson’s disease, Multiple Sclerosis, vascular dementia, depression, anxiety, and schizophrenia. This book will appeal to anyone looking to learn more about how nutrition affects brain health.

```html
<!DOCTYPE html>
<html lang="en">
<head>
<meta charset="utf-8">
<title>Meals Across the Decades — Book Cover</title>
<link rel="stylesheet" href="https://fonts.googleapis.com/css2?family=Crimson+Pro:wght@500;600;700&family=Roboto+Condensed:wght@400;500&display=swap">
<style>
  :root {
    --backdrop: #8a8a8a;
    --paper: #ffffff;
    --navy: #0b3577;
    --green: #0f9d4a;
    --ink: #111111;
    --band-text: #ffffff;
  }
  * { margin: 0; padding: 0; box-sizing: border-box; }
  html, body {
    width: 1200px;
    height: 800px;
    overflow: hidden;
    background: var(--backdrop);
  }
  .stage {
    width: 1200px;
    height: 800px;
    display: flex;
    align-items: center;
    justify-content: center;
  }
  .cover {
    position: relative;
    width: 480px;
    height: 730px;
    background: var(--paper);
    display: flex;
    flex-direction: column;
    align-items: center;
  }
  .title {
    margin-top: 62px;
    text-align: center;
    font-family: "Crimson Pro", Georgia, serif;
    color: var(--navy);
    line-height: 0.92;
    text-transform: uppercase;
  }
  .title span { display: block; }
  .title .line-small { font-size: 50px; font-weight: 500; letter-spacing: 0.5px; }
  .title .line-accent { font-size: 64px; font-weight: 700; color: var(--green); letter-spacing: 1px; }
  .title .line-mid { font-size: 56px; font-weight: 500; }
  .title .line-large { font-size: 68px; font-weight: 700; letter-spacing: 1px; }
  .brain-art {
    margin-top: 22px;
    width: 320px;
    height: 240px;
    border-radius: 46% 46% 40% 40%;
    background:
      radial-gradient(circle at 35% 55%, rgba(226, 40, 40, 0.75), transparent 35%),
      radial-gradient(circle at 55% 50%, rgba(40, 170, 60, 0.75), transparent 35%),
      radial-gradient(circle at 70% 60%, rgba(240, 220, 40, 0.7), transparent 38%),
      radial-gradient(circle at 45% 30%, rgba(80, 200, 230, 0.6), transparent 40%),
      radial-gradient(ellipse at center, rgba(245, 235, 120, 0.5), transparent 70%);
  }
  .subtitle {
    margin-top: 24px;
    font-family: "Roboto Condensed", "Arial Narrow", sans-serif;
    font-weight: 500;
    font-size: 17px;
    color: var(--ink);
    letter-spacing: 0.2px;
    text-transform: uppercase;
  }
  .editor-band {
    position: absolute;
    left: 0;
    bottom: 0;
    width: 100%;
    height: 68px;
    background: var(--navy);
    display: flex;
    align-items: center;
    justify-content: center;
    font-family: "Roboto Condensed", "Arial Narrow", sans-serif;
    color: var(--band-text);
    font-size: 25px;
    letter-spacing: 1px;
  }
  .editor-band .editor-name { text-transform: uppercase; margin-left: 8px; }
</style>
</head>
<body>
  <main class="stage">
    <article class="cover">
      <h1 class="title">
        <span class="line-small">Meals</span>
        <span class="line-accent">Across</span>
        <span class="line-mid">The</span>
        <span class="line-large">Decades</span>
      </h1>
      <div class="brain-art" role="img" aria-label="Line drawing of a brain seen from above, splashed with red, green, yellow and blue paint"></div>
      <p class="subtitle">A Companion Guide to Dietary Brain Science Today</p>
      <footer class="editor-band">Edited by <span class="editor-name">Odelia R. Vantrosk</span></footer>
    </article>
  </main>
</body>
</html>
```